Varlow Landscaping

Create a website for a new landscaping company. I have a logo already and description of services offered. I have a website that I would like all inquiries and appointments to get forwarded to. I need just need it well organized so that a husband and wife team can manage it easily. This is a company that will continue to grow over time and will need to add more services under new tabs over time. If you need the email where appointments and inquiries should go please send me a message.
Services offered are: Weekly/bi weekly mowing, weed eating and edging, Plant installation pinestraw & mulch installation, weed & feed, leaf removal and yard clean up.

```html
<!DOCTYPE html>
<html lang="en">
<head>
<meta charset="utf-8">
<title>Varlow Landscaping – Lawn Care &amp; Landscaping</title>
<link rel="stylesheet" href="https://fonts.googleapis.com/css2?family=Montserrat:ital,wght@0,400;0,500;0,600;0,700;1,400&display=swap">
<style>
:root{
  --green-bar:#2a7a1f;
  --forest:#2f4f2b;
  --forest-mid:#3a5c35;
  --forest-deep:#1f3520;
  --footer:#172417;
  --leaf:#5a8f3a;
  --white:#ffffff;
  --muted:#d7e2d2;
  --star:#f4b400;
  --ink:#3b3b3b;
}
*{box-sizing:border-box;margin:0;padding:0}
html,body{width:1200px;height:4744px;overflow:hidden}
body{font-family:"Montserrat",sans-serif;color:var(--white);background:var(--forest);position:relative}
.abs{position:absolute}
.btn{position:absolute;border:1.5px solid var(--white);border-radius:20px;color:var(--white);font-size:13px;font-weight:600;display:flex;align-items:center;justify-content:center;height:38px}
.photo{position:absolute}

/* top bar */
.topbar{position:absolute;left:0;top:0;width:1200px;height:37px;background:var(--green-bar);font-size:12px}
.social-dot{position:absolute;top:11px;width:14px;height:14px;border-radius:50%;background:var(--white)}
.topbar .contact{position:absolute;top:11px;display:flex;align-items:center;gap:7px}

/* hero */
.hero{position:absolute;left:0;top:37px;width:1200px;height:733px}
.hero .photo{inset:0;background:linear-gradient(100deg,#2d3a24 0%,#3d5a2a 35%,#6b7d4a 60%,#4a6233 80%,#2f3f22 100%)}
.hero-circle{position:absolute;left:125px;top:148px;width:330px;height:350px;border-radius:50%;background:#2d6a24;opacity:.9}
.nav{position:absolute;left:0;top:0;width:1200px;height:100px}
.logo{position:absolute;display:flex;align-items:center;gap:8px;font-weight:700;color:var(--white)}
.logo .mark{width:22px;height:22px;border-radius:50%;background:var(--white)}
.menu{position:absolute;top:33px;font-size:13px;font-weight:500}
.menu.active::after{content:"";position:absolute;left:0;right:0;top:22px;height:2px;background:var(--leaf)}
.hero h1{position:absolute;left:160px;top:283px;font-size:46px;line-height:55px;font-weight:700}
.hero p{position:absolute;left:160px;top:396px;width:500px;font-size:13px;line-height:17px}
.arrow{position:absolute;top:355px}
.dots{position:absolute;left:560px;top:706px;display:flex;gap:8px}
.dots span{width:24px;height:3px;background:rgba(255,255,255,.5)}
.dots span.on{background:var(--white)}

/* about */
.about{position:absolute;left:0;top:770px;width:1200px;height:642px;background:var(--forest-mid)}
.eyebrow{font-size:13px}
.about h2{position:absolute;left:160px;top:155px;font-size:29px;font-weight:700}
.about p{position:absolute;left:160px;top:208px;width:375px;font-size:13px;line-height:19.5px;color:var(--muted)}

/* services */
.services{position:absolute;left:0;top:1412px;width:1200px;height:852px;background:var(--forest)}
.sec-title{position:absolute;left:0;width:1200px;text-align:center;font-size:30px;font-weight:700}
.sec-sub{position:absolute;left:0;width:1200px;text-align:center;font-size:13px;line-height:18px;color:var(--muted)}
.svc-text{position:absolute;width:396px;height:155px;padding:18px 54px 0}
.svc-text h3{font-size:15px;font-weight:700;margin-bottom:12px}
.svc-text p{font-size:11.5px;line-height:16px;color:var(--muted)}
.svc-text .more{display:flex;align-items:center;gap:8px;margin-top:12px;font-size:11px;font-weight:600}

/* works */
.works{position:absolute;left:0;top:2264px;width:1200px;height:966px;background:var(--forest-mid)}
.work-caption{position:absolute;left:621px;top:738px;width:408px;height:72px;background:rgba(45,70,40,.85);display:flex;align-items:center;padding:0 22px;gap:30px}
.work-caption h4{font-size:19px;line-height:22px;font-weight:700;width:130px}
.work-caption p{font-size:11.5px;line-height:17px}

/* testimonials */
.reviews{position:absolute;left:0;top:3230px;width:1200px;height:590px}
.reviews .photo{inset:0;background:linear-gradient(90deg,#2c3f27,#42603a 50%,#2c3f27)}
.card{position:absolute;top:206px;width:276px;height:144px;background:rgba(255,255,255,.96);border-radius:4px;padding:18px 20px;color:var(--ink)}
.card .rating{display:flex;align-items:center;gap:8px;font-size:13px;font-weight:600;color:#222}
.card .stars{color:var(--star);letter-spacing:2px}
.card .g{position:absolute;right:16px;top:20px;width:14px;height:14px;border-radius:50%;border:2px solid #4285f4}
.card p{margin-top:16px;font-size:11.5px;font-style:italic;line-height:20px;color:#666}
.person{position:absolute;top:396px;display:flex;align-items:center;gap:18px;font-size:14px}
.person .avatar{width:48px;height:48px;border-radius:50%;background:linear-gradient(135deg,#c9b6a3,#7d6a5a);border:2px solid var(--white)}
.person strong{display:block;font-weight:700}

/* contact */
.contact-sec{position:absolute;left:0;top:3820px;width:1200px;height:600px;background:var(--forest)}
.field{position:absolute;background:var(--white);color:#7a7a7a;font-size:13px;padding:16px 16px}
.grass{position:absolute;left:0;top:510px;width:1200px;height:90px;background:linear-gradient(180deg,rgba(23,36,23,0),#1c2d1b 55%,var(--footer))}

/* footer */
.footer{position:absolute;left:0;top:4420px;width:1200px;height:324px;background:var(--footer)}
.footer h5{position:absolute;top:100px;font-size:15px;font-weight:700}
.footer ul{position:absolute;top:140px;list-style:none;font-size:13px;line-height:37px}
.fcontact{position:absolute;left:847px;top:140px;font-size:13px}
.fcontact div{display:flex;align-items:center;gap:14px;height:37px}
.ic{width:24px;height:24px;border-radius:50%;background:var(--green-bar);display:flex;align-items:center;justify-content:center}
</style>
</head>
<body>

<header class="topbar">
  <span class="social-dot" style="left:160px"></span>
  <span class="social-dot" style="left:195px"></span>
  <span class="social-dot" style="left:234px"></span>
  <span class="contact" style="left:693px">
    <svg width="12" height="12" viewBox="0 0 24 24"><path fill="#fff" d="M6.6 10.8a15 15 0 0 0 6.6 6.6l2.2-2.2c.3-.3.7-.4 1-.2 1.1.4 2.3.6 3.6.6.6 0 1 .4 1 1V20c0 .6-.4 1-1 1C10.6 21 3 13.4 3 4c0-.6.4-1 1-1h3.5c.6 0 1 .4 1 1 0 1.3.2 2.5.6 3.6.1.3 0 .7-.2 1z"/></svg>
    +1 555 014 2290</span>
  <span class="contact" style="left:838px">
    <svg width="13" height="10" viewBox="0 0 24 18"><rect width="24" height="18" rx="2" fill="#fff"/><path d="M1 2l11 8 11-8" stroke="#2a7a1f" stroke-width="2" fill="none"/></svg>
    hello@varlowyards.com</span>
</header>

<section class="hero">
  <div class="photo" role="img" aria-label="Smiling gardener pushing a red lawn mower across a green lawn"></div>
  <div class="hero-circle"></div>
  <nav class="nav">
    <div class="logo" style="left:160px;top:38px;font-size:17px"><span class="mark"></span>Varlow</div>
    <span class="menu active" style="left:322px;top:33px">Home</span>
    <span class="menu" style="left:398px">About Us</span>
    <span class="menu" style="left:494px">Services</span>
    <span class="menu" style="left:586px">Projects</span>
    <span class="menu" style="left:676px">Testimonial</span>
    <span class="menu" style="left:790px">Contact Us</span>
    <span class="btn" style="left:893px;top:22px;width:145px;height:38px">Get In Touch</span>
  </nav>
  <h1>Reliable Lawn Care &amp;<br>Landscaping Services</h1>
  <p>Elevate your environment with our unrivaled expertise and passion for excellence! Our rich legacy to your green dreams into reality.</p>
  <span class="btn" style="left:160px;top:455px;width:140px">Learn More</span>
  <svg class="arrow" style="left:30px" width="14" height="24" viewBox="0 0 14 24"><path d="M12 2 2 12l10 10" stroke="#fff" stroke-width="2" fill="none"/></svg>
  <svg class="arrow" style="left:1156px" width="14" height="24" viewBox="0 0 14 24"><path d="m2 2 10 10L2 22" stroke="#fff" stroke-width="2" fill="none"/></svg>
  <div class="dots"><span class="on"></span><span></span><span></span></div>
</section>

<section class="about">
  <span class="abs eyebrow" style="left:160px;top:128px">About Us</span>
  <h2>We Provide Best Services</h2>
  <p>Lorem Ipsum is simply dummy text of the printing and typesetting industry. Lorem Ipsum has been the industry's standard dummy text ever since the 1500s, when an unknown printer took a galley of type and scrambled it to make a type specimen book. It has survived not only five centuries, but also the leap into electronic typesetting, remaining essentially unchanged. Lorem Ipsum is simply dummy text of the printing and typesetting industry. Lorem Ipsum has been the industry's standard dummy text ever since the 1500s, when an unknown printer took a galley of type and scrambled it to make a unchanged.</p>
  <span class="btn" style="left:160px;top:470px;width:140px">Learn More</span>
  <div class="photo" style="left:636px;top:60px;width:402px;height:440px;background:linear-gradient(160deg,#8fae5a,#4f7a2e 55%,#2f5a22)" role="img" aria-label="Gardener in cap and ear protection trimming a hedge"></div>
  <div class="photo" style="left:583px;top:405px;width:215px;height:172px;background:linear-gradient(150deg,#5f8a3c,#2e5a2a);border:3px solid var(--forest-mid)" role="img" aria-label="Two gardeners in aprons tending potted plants"></div>
</section>

<section class="services">
  <h2 class="sec-title" style="top:50px">Our Services</h2>
  <p class="sec-sub" style="top:98px">Discover tailored garden and landscape solutions.</p>

  <div class="photo" style="left:0;top:160px;width:396px;height:396px;background:linear-gradient(170deg,#6d9b3e,#3f7a25)" role="img" aria-label="Red lawn mower on freshly cut grass"></div>
  <div class="svc-text" style="left:0;top:556px">
    <h3>Weekly/Bi Weekly Mowing</h3>
    <p>Investment Planning Working with thousands of business companies around consectetur adipissed do eius mod tempor incididunt at laboret.</p>
    <span class="more">LEARN MORE <svg width="12" height="10" viewBox="0 0 12 10"><path d="M0 5h10M6 1l4 4-4 4" stroke="#7bc043" stroke-width="1.6" fill="none"/></svg></span>
  </div>

  <div class="svc-text" style="left:396px;top:160px;width:408px">
    <h3>Weed Eating and Edging</h3>
    <p>Investment Planning Working with thousands of business companies around consectetur adipissed do eius mod tempor incididunt at laboret.</p>
    <span class="more">LEARN MORE <svg width="12" height="10" viewBox="0 0 12 10"><path d="M0 5h10M6 1l4 4-4 4" stroke="#7bc043" stroke-width="1.6" fill="none"/></svg></span>
  </div>
  <div class="photo" style="left:396px;top:315px;width:408px;height:395px;background:linear-gradient(160deg,#4a3a2a,#2a2018)" role="img" aria-label="Hand pulling a weed from soil with a small tool"></div>

  <div class="photo" style="left:804px;top:160px;width:396px;height:396px;background:linear-gradient(170deg,#8aa864,#4f6f35)" role="img" aria-label="Two people clearing leaves and branches in a yard"></div>
  <div class="svc-text" style="left:804px;top:556px">
    <h3>Leaf Removal and yard cleana</h3>
    <p>Investment Planning Working with thousands of business companies around consectetur adipissed do eius mod tempor incididunt at laboret.</p>
    <span class="more">LEARN MORE <svg width="12" height="10" viewBox="0 0 12 10"><path d="M0 5h10M6 1l4 4-4 4" stroke="#7bc043" stroke-width="1.6" fill="none"/></svg></span>
  </div>

  <span class="btn" style="left:520px;top:763px;width:160px">View All Services</span>
</section>

<section class="works">
  <h2 class="sec-title" style="top:52px">Our Works</h2>
  <p class="sec-sub" style="top:107px;left:350px;width:500px">Discover tailored garden and landscape solutions. and mect values, vemioreal through tionrgs or venuersiond abilites.</p>
  <div class="photo" style="left:160px;top:188px;width:430px;height:300px;background:linear-gradient(150deg,#6f9a48,#2f5a25)" role="img" aria-label="Gloved hands pruning a green shrub"></div>
  <div class="photo" style="left:609px;top:188px;width:429px;height:300px;background:linear-gradient(170deg,#a4bf78,#4f7a33)" role="img" aria-label="Gardener holding a hedge trimmer beside a hedge"></div>
  <div class="photo" style="left:160px;top:504px;width:430px;height:300px;background:linear-gradient(170deg,#9fb5a0,#5b8a35 50%,#3f7424)" role="img" aria-label="Worker trimming a hedge in front of a house"></div>
  <div class="photo" style="left:609px;top:504px;width:429px;height:300px;background:linear-gradient(160deg,#7ea352,#3f6a2c)" role="img" aria-label="Woman planting flowers in a garden bed"></div>
  <div class="work-caption">
    <h4>Garden Maintenance</h4>
    <p>Varlow Enterprise gives comsiders reging foundations and mect tionrgs or venuersiond abilites.</p>
  </div>
  <span class="btn" style="left:520px;top:864px;width:160px">View All Works</span>
</section>

<section class="reviews">
  <div class="photo" role="img" aria-label="Gardener kneeling among shrubs, softly darkened background"></div>
  <h2 class="sec-title" style="top:76px">What Our Customers Are Saying</h2>
  <p class="sec-sub" style="top:130px;left:350px;width:500px">Varlow gives comsiders reging foundations and mect values, vemioreal through tionrgs or venuersiond abilites.</p>

  <div class="card" style="left:14px"><div class="rating"><span class="stars">★★★★★</span>5.0</div><span class="g"></span><p>We believe in four pillars of influence that drive our growth. This is ingrained in everything we do We use</p></div>
  <div class="card" style="left:314px"><div class="rating"><span class="stars">★★★★★</span>5.0</div><span class="g"></span><p>We believe in four pillars of influence that drive our growth. This is ingrained in everything we do We use</p></div>
  <div class="card" style="left:613px"><div class="rating"><span class="stars">★★★★★</span>5.0</div><span class="g"></span><p>We believe in four pillars of influence that drive our growth. This is ingrained in everything we do We use</p></div>
  <div class="card" style="left:913px"><div class="rating"><span class="stars">★★★★★</span>5.0</div><span class="g"></span><p>We believe in four pillars of influence that drive our growth. This is ingrained in everything we do We use</p></div>

  <div class="person" style="left:28px"><span class="avatar" role="img" aria-label="Customer portrait"></span><span>Mara Ellison<strong>Medical Assistant</strong></span></div>
  <div class="person" style="left:328px"><span class="avatar" role="img" aria-label="Customer portrait"></span><span>Mara Ellison<strong>Medical Assistant</strong></span></div>
  <div class="person" style="left:627px"><span class="avatar" role="img" aria-label="Customer portrait"></span><span>Mara Ellison<strong>Medical Assistant</strong></span></div>
  <div class="person" style="left:927px"><span class="avatar" role="img" aria-label="Customer portrait"></span><span>Mara Ellison<strong>Medical Assistant</strong></span></div>

  <span class="btn" style="left:520px;top:507px;width:160px;height:36px">See All Reviews</span>
</section>

<section class="contact-sec">
  <h2 class="sec-title" style="top:52px">Get In Touch</h2>
  <div class="field" style="left:216px;top:127px;width:372px;height:49px">First Name</div>
  <div class="field" style="left:611px;top:127px;width:373px;height:49px">Last Name</div>
  <div class="field" style="left:216px;top:196px;width:372px;height:49px">Email Address</div>
  <div class="field" style="left:611px;top:196px;width:373px;height:49px">Phone Number</div>
  <div class="field" style="left:216px;top:265px;width:768px;height:165px">Message</div>
  <span class="btn" style="left:520px;top:445px;width:160px;height:36px">SUBMIT</span>
  <div class="grass" role="img" aria-label="Dark silhouette of grass and butterflies along the bottom edge"></div>
</section>

<footer class="footer">
  <div class="logo" style="left:170px;top:90px;font-size:30px;color:#7bc043"><span class="mark" style="background:#7bc043;width:26px;height:26px"></span>Varlow</div>
  <span class="abs" style="left:160px;top:150px;font-size:12px;color:#7bc043">LAWN CARE &amp; LANDSCAPING</span>
  <span class="social-dot" style="left:204px;top:244px"></span>
  <span class="social-dot" style="left:248px;top:244px"></span>
  <span class="social-dot" style="left:290px;top:244px"></span>

  <h5 style="left:437px">Quick Links</h5>
  <ul style="left:437px"><li>Home</li><li>About Us</li><li>Services</li><li>Contact Us</li></ul>

  <h5 style="left:612px">Services</h5>
  <ul style="left:612px"><li>Weekly/Bi Weekly Mowing</li><li>Weed Eating and Edging</li><li>Plant Installation Pinestraw</li><li>Weed &amp; Feed</li></ul>

  <h5 style="left:847px">Contact Us</h5>
  <div class="fcontact">
    <div><span class="ic"><svg width="11" height="11" viewBox="0 0 24 24"><path fill="#fff" d="M6.6 10.8a15 15 0 0 0 6.6 6.6l2.2-2.2c.3-.3.7-.4 1-.2 1.1.4 2.3.6 3.6.6.6 0 1 .4 1 1V20c0 .6-.4 1-1 1C10.6 21 3 13.4 3 4c0-.6.4-1 1-1h3.5c.6 0 1 .4 1 1 0 1.3.2 2.5.6 3.6.1.3 0 .7-.2 1z"/></svg></span>555-014-2290</div>
    <div><span class="ic"><svg width="11" height="9" viewBox="0 0 24 18"><rect width="24" height="18" rx="2" fill="#fff"/><path d="M1 2l11 8 11-8" stroke="#2a7a1f" stroke-width="2" fill="none"/></svg></span>info@varlowyards.com</div>
    <div><span class="ic"><svg width="10" height="12" viewBox="0 0 20 24"><path fill="#fff" d="M10 0a8 8 0 0 0-8 8c0 6 8 16 8 16s8-10 8-16a8 8 0 0 0-8-8zm0 11a3 3 0 1 1 0-6 3 3 0 0 1 0 6z"/></svg></span>122, Lorem ipsum dolird</div>
  </div>
</footer>

</body>
</html>
```